3rd Annual Maple & Clover Fundraiser

This is our 3rd Annual Maple & Clover Dog Wash Extravagana to support Circle of Harlow Ridge Pet Center. Please see the attached flyer for the 2nd Annual. We loved this flyer! Please revamp with our logo attached and the new content provided. Let's keep to the same colors as the 2nd Annual flyer-no change. Date: Saturday April 25th 2020 10A-1PM. Rain Date: May 2nd. Same address as 2nd Annual.

Other font styles liked:
• See 2nd Annual Flyer

Colors
add136
e34297
6b449b

Requirements
Must have
• See attached 2nd annual flyer including colors
Nice to have

```html
<!DOCTYPE html>
<html lang="en">
<head>
<meta charset="utf-8">
<title>3rd Annual Maple &amp; Clover Dog Wash Extravaganza</title>
<link href="https://fonts.googleapis.com/css2?family=Arimo:ital,wght@0,400;0,700;1,400&family=Patrick+Hand+SC&display=swap" rel="stylesheet">
<style>
  :root {
    --green: #add136;
    --pink: #e34297;
    --purple: #6b449b;
    --purple-mid: #8a6bb5;
    --lilac: #cbb8df;
    --ink: #1d1d1d;
    --white: #ffffff;
  }
  html, body { margin: 0; padding: 0; overflow: hidden; background: var(--white); }
  .flyer {
    position: relative; width: 815px; height: 1200px; overflow: hidden;
    background: var(--white); font-family: "Arimo", Arial, sans-serif; color: var(--ink);
  }
  .abs { position: absolute; }
  .hand { font-family: "Patrick Hand SC", "Comic Sans MS", cursive; }

  .brand-name { left: 50px; top: 190px; font-size: 44px; font-weight: 700; color: var(--purple-mid); display: flex; align-items: center; gap: 10px; white-space: nowrap; }
  .brand-dot { width: 18px; height: 18px; border-radius: 50%; background: var(--green); }
  .event-title { left: 52px; top: 244px; font-size: 13px; font-weight: 700; letter-spacing: 3.2px; color: var(--pink); text-transform: uppercase; white-space: nowrap; }
  .center-name { left: 470px; top: 128px; width: 238px; text-align: center; font-size: 25px; font-weight: 700; line-height: 1.2; color: var(--ink); }

  .photo-band { left: 0; top: 267px; width: 815px; height: 356px;
    background:
      linear-gradient(90deg, rgba(238,110,40,0.55) 6%, rgba(30,30,30,0.45) 22%, rgba(40,40,40,0.5) 38%, rgba(70,140,210,0.55) 52%, rgba(160,110,60,0.6) 64%, rgba(235,230,235,0.5) 78%, rgba(200,195,170,0.55) 92%) 0 150px / 815px 206px no-repeat,
      linear-gradient(180deg, #a9c9e6 0%, #9cc08a 30%, #6b8c55 48%, #8a8a84 100%); }
  .strip { top: 623px; height: 13px; }
  .strip.pink { left: 0; width: 300px; background: var(--pink); }
  .strip.purple { left: 300px; width: 270px; background: var(--purple-mid); }
  .strip.green { left: 570px; width: 245px; background: var(--green); }

  .section-title { top: 644px; font-size: 30px; color: var(--pink); letter-spacing: 0.5px; white-space: nowrap; }
  .info-box { top: 682px; height: 98px; border: 3px solid var(--green); border-radius: 8px; box-sizing: border-box; }
  .info-box.when { left: 24px; width: 376px; padding: 8px 0 0 26px; }
  .info-box.where { left: 421px; width: 374px; padding: 10px 0 0 32px; }
  .row { display: flex; align-items: baseline; gap: 12px; line-height: 25px; }
  .label { color: var(--purple-mid); font-size: 25px; width: 66px; text-align: right; }
  .value { font-size: 20px; line-height: 25px; }

  .features { top: 810px; font-size: 19px; line-height: 23px; }
  .features ul { list-style: none; margin: 0; padding: 0; }
  .features li { position: relative; padding-left: 34px; white-space: nowrap; }
  .tick-icon { position: absolute; left: 0; top: 1px; width: 24px; height: 20px; }

  .donate-line { left: 300px; top: 906px; white-space: nowrap; }
  .donate-line .hand { font-size: 25px; color: var(--pink); }
  .donate-line .url { font-size: 17px; font-style: italic; }
  .donate-btn { left: 415px; top: 946px; width: 223px; height: 39px; border-radius: 20px;
    background: var(--green); color: var(--white); font-size: 18px; font-weight: 700;
    display: flex; align-items: center; justify-content: center; }

  .contact-name { top: 1005px; font-size: 28px; color: var(--pink); white-space: nowrap; }
  .contact-info { top: 1043px; font-size: 13px; line-height: 17px; white-space: nowrap; }
  .sig-name { left: 350px; top: 1105px; width: 170px; text-align: center; font-size: 22px; font-weight: 700; color: var(--purple); }
  .partner-name { left: 610px; top: 1088px; width: 150px; text-align: center; font-size: 17px; font-weight: 700; line-height: 1.2; color: var(--ink); }
</style>
</head>
<body>
<div class="flyer">

  <svg class="abs" style="left:0;top:0" width="815" height="300" aria-hidden="true">
    <circle cx="43" cy="80" r="34" fill="var(--lilac)"/>
    <circle cx="140" cy="88" r="50" fill="var(--lilac)"/>
    <circle cx="210" cy="34" r="36" fill="var(--lilac)"/>
    <circle cx="130" cy="12" r="20" fill="var(--lilac)"/>
    <circle cx="305" cy="190" r="140" fill="var(--purple-mid)"/>
    <rect x="0" y="115" width="435" height="152" fill="var(--white)"/>
    <polygon points="370,0 815,0 815,267 470,267" fill="var(--purple-mid)"/>
    <circle cx="760" cy="60" r="55" fill="#9a7fc0"/>
    <circle cx="589" cy="181" r="133" fill="var(--white)" stroke="var(--green)" stroke-width="4"/>
  </svg>

  <div class="abs brand-name"><span class="brand-dot"></span>Maple &amp; Clover</div>
  <div class="abs event-title">3rd Annual Dog Wash Extravaganza</div>
  <div class="abs center-name">Circle of Harlow Ridge Pet Center</div>

  <div class="abs photo-band" role="img" aria-label="Group photo of smiling teen volunteers outdoors beside a costumed dog mascot"></div>
  <div class="abs strip pink"></div>
  <div class="abs strip purple"></div>
  <div class="abs strip green"></div>

  <div class="abs section-title hand" style="left:30px">A Family Fun Event For All Ages</div>
  <div class="abs section-title hand" style="left:560px">Location</div>

  <div class="abs info-box when">
    <div class="row"><span class="label">Date:</span><span class="value">Saturday April 25th 2020</span></div>
    <div class="row"><span class="label"></span><span class="value">Rain Date: May 2nd</span></div>
    <div class="row" style="margin-top:2px"><span class="label">Time:</span><span class="value">10A-1PM</span></div>
  </div>
  <div class="abs info-box where">
    <div class="value">Larkin Realty , 118 Orchard Lane<br>Ave. Harlow Ridge FL 3281<br>Brookfield Town center</div>
  </div>

  <svg class="abs" style="left:0;top:787px" width="815" height="413" aria-hidden="true">
    <defs>
      <linearGradient id="photoTone" x1="0" y1="0" x2="1" y2="1">
        <stop offset="0" stop-color="#bcd3e8"/>
        <stop offset="0.35" stop-color="#e6d36a"/>
        <stop offset="0.55" stop-color="#d98a9a"/>
        <stop offset="0.8" stop-color="#6f6a66"/>
        <stop offset="1" stop-color="#3f3c3a"/>
      </linearGradient>
      <linearGradient id="insetTone" x1="0" y1="0" x2="1" y2="1">
        <stop offset="0" stop-color="#a97a4a"/>
        <stop offset="0.6" stop-color="#e58a4a"/>
        <stop offset="1" stop-color="#e9e6f0"/>
      </linearGradient>
    </defs>
    <path d="M0 0 H250 Q240 210 335 413 H0 Z" fill="url(#photoTone)" role="img" aria-label="Photo of a boy, a girl and a man in a cap with a dark dog at the event"/>
    <path d="M258 0 Q246 210 342 413" fill="none" stroke="var(--purple-mid)" stroke-width="14"/>
  </svg>
  <svg class="abs" style="left:92px;top:810px" width="146" height="146" role="img" aria-label="Inset photo of a volunteer and the dog mascot holding a free doggie wash sign">
    <circle cx="73" cy="73" r="68" fill="url(#insetTone)" stroke="var(--white)" stroke-width="6"/>
  </svg>

  <div class="abs features" style="left:310px">
    <ul>
      <li><svg class="tick-icon" viewBox="0 0 24 20"><path d="M2 10 L9 17 L22 2" fill="none" stroke="var(--pink)" stroke-width="4" stroke-linecap="round" stroke-linejoin="round"/></svg>FREE Doggie Wash</li>
      <li><svg class="tick-icon" viewBox="0 0 24 20"><path d="M2 10 L9 17 L22 2" fill="none" stroke="var(--pink)" stroke-width="4" stroke-linecap="round" stroke-linejoin="round"/></svg>Food &amp; Beverages</li>
      <li><svg class="tick-icon" viewBox="0 0 24 20"><path d="M2 10 L9 17 L22 2" fill="none" stroke="var(--pink)" stroke-width="4" stroke-linecap="round" stroke-linejoin="round"/></svg>Vendors</li>
      <li>(FREE give-a-ways)</li>
    </ul>
  </div>
  <div class="abs features" style="left:536px">
    <ul>
      <li><svg class="tick-icon" viewBox="0 0 24 20"><path d="M2 10 L9 17 L22 2" fill="none" stroke="var(--pink)" stroke-width="4" stroke-linecap="round" stroke-linejoin="round"/></svg>Raffle Drawings</li>
      <li><svg class="tick-icon" viewBox="0 0 24 20"><path d="M2 10 L9 17 L22 2" fill="none" stroke="var(--pink)" stroke-width="4" stroke-linecap="round" stroke-linejoin="round"/></svg>Grand Prize</li>
      <li><svg class="tick-icon" viewBox="0 0 24 20"><path d="M2 10 L9 17 L22 2" fill="none" stroke="var(--pink)" stroke-width="4" stroke-linecap="round" stroke-linejoin="round"/></svg>Donations Welcome</li>
      <li><svg class="tick-icon" viewBox="0 0 24 20"><path d="M2 10 L9 17 L22 2" fill="none" stroke="var(--pink)" stroke-width="4" stroke-linecap="round" stroke-linejoin="round"/></svg>Adoptions by CHRPC</li>
    </ul>
  </div>

  <div class="abs donate-line"><span class="hand">To Make a Donations:</span> <span class="url">https://www.harlowridgepets.org/give/</span></div>
  <div class="abs donate-btn">CLICK: DONATE</div>

  <div class="abs contact-name hand" style="left:332px">Marian Tellis</div>
  <div class="abs contact-info" style="left:336px">Larkin Realty Corp. 555.210.4418<br>mariantellis@larkinrealtycorp.com</div>
  <div class="abs contact-name hand" style="left:597px">Dana Whitcombe</div>
  <div class="abs contact-info" style="left:601px">CHRPC. 555.30417762<br>dana-whitcombe@mailbox.net</div>

  <div class="abs sig-name">Marian Tellis</div>
  <div class="abs partner-name">Circle of Harlow Ridge Pet Center</div>
</div>
</body>
</html>
```